Breast Cancer Car Donation Website Design

Please create a new one page website design.

Current site: http://www.giveautopinkribbon.org/

The NEW website address will be RidesforPinkHope.org

Use these sites for an idea of what I am looking for. I like these sites best: motorsforheroes.org and autosforservice.org

Coding

Coded - Design and coding required

Number of Pages Required

1 page

```html
<!DOCTYPE html>
<html lang="en">
<head>
<meta charset="utf-8">
<title>Pink Road Foundation – Donate Your Car</title>
<link href="https://fonts.googleapis.com/css2?family=Raleway:wght@400;600;700;800&family=Open+Sans:wght@400;600;700&family=Cinzel:wght@600&display=swap" rel="stylesheet">
<style>
:root{
  --pink:#e8157f;
  --pink-soft:#f45aa4;
  --sky:#a9cbe9;
  --sky-dark:#7fa8d1;
  --ink:#2b2b2b;
  --muted:#6f6f6f;
  --field:#ececec;
  --line:#dcdcdc;
  --footer:#2f2f2f;
  --footer-deep:#262626;
  --white:#fff;
}
*{box-sizing:border-box;margin:0;padding:0}
html,body{width:1200px;height:3291px;overflow:hidden}
body{font-family:"Open Sans",Arial,sans-serif;color:var(--ink);background:var(--white);position:relative}
.abs{position:absolute}
.btn{display:inline-block;border-radius:4px;color:#fff;font-family:"Open Sans",sans-serif;font-weight:700;text-align:center}
.btn-pink{background:linear-gradient(var(--pink-soft),var(--pink))}
.btn-sky{background:linear-gradient(#b8d4ee,var(--sky-dark))}

/* header */
.topbar{left:0;top:0;width:1200px;height:75px;background:linear-gradient(90deg,#f07ab3,#f28fbe 60%,#f4a2c9)}
.navbar{left:0;top:75px;width:1200px;height:28px;background:var(--sky)}
.brand{left:150px;top:0;width:175px;height:103px;background:#fff;display:flex;flex-direction:column;align-items:center;justify-content:center;gap:6px;box-shadow:0 2px 4px rgba(0,0,0,.15)}
.brand-dot{width:34px;height:34px;border-radius:50%;background:var(--pink)}
.brand-name{font-family:"Open Sans",sans-serif;font-weight:700;font-size:14px;color:var(--pink);text-align:center;line-height:1.15}
.tagline{left:333px;top:32px;color:#fff;font-style:italic;font-weight:600;font-size:13px}
.phone{left:698px;top:28px;color:#fff;font-size:12px;font-weight:600}
.phone b{font-size:19px;margin-left:6px;font-weight:700}
.top-cta{left:942px;top:27px;width:108px;height:32px;line-height:32px;font-size:12px;border-radius:3px}
.menu{left:333px;top:75px;height:28px;display:flex;gap:0;list-style:none}
.menu li{font-size:11px;font-weight:600;color:#fff;line-height:28px;padding:0 21px;text-transform:uppercase}
.menu li.active{color:#1f3d5c}

/* hero */
.hero-photo{left:0;top:103px;width:1200px;height:531px;background:linear-gradient(100deg,#3d3d3d,#8a8a8a 40%,#5a5a5a 70%,#6c6c6c)}
.hero-ribbon{left:180px;top:120px;width:380px;height:500px;background:radial-gradient(ellipse at 50% 50%,rgba(236,60,150,.9),rgba(236,60,150,0) 65%)}
.hero-form{left:605px;top:165px;width:446px;height:419px;background:#fff;box-shadow:0 4px 14px rgba(0,0,0,.3)}
.hero-form-head{height:118px;background:linear-gradient(#9cc4e8,#c7dcf0);color:#fff;text-align:center;padding-top:22px}
.hero-form-head h2{font-family:"Raleway",sans-serif;font-weight:800;font-size:25px;letter-spacing:.5px}
.hero-form-head p{font-size:9.5px;margin-top:12px}
.fields{display:grid;grid-template-columns:1fr 1fr;gap:14px 20px;padding:18px 24px 0}
.field{height:30px;background:var(--field);border-radius:3px;font-size:10px;color:#999;padding:0 12px;line-height:30px;position:relative}
.field::after{content:"";position:absolute;right:10px;top:11px;width:8px;height:8px;background:#bbb;border-radius:2px}
.hero-cta{position:absolute;left:96px;top:333px;width:254px;height:40px;line-height:40px;font-size:16px}
.hero-call{position:absolute;left:0;top:385px;width:446px;text-align:center;font-size:13px;font-weight:700}
.hero-call span{color:var(--pink)}

/* donate */
.sec-title{font-family:"Raleway",sans-serif;font-weight:600;font-size:31px;text-align:center;width:1200px;left:0}
.sec-sub{left:0;width:1200px;text-align:center;font-size:15px;color:var(--muted)}
.feature{width:260px;text-align:center}
.feature-ring{width:124px;height:124px;margin:0 auto;border-radius:50%;border:2px dashed var(--pink-soft);display:flex;align-items:center;justify-content:center}
.feature-ring span{width:106px;height:106px;border-radius:50%;background:var(--pink);display:flex;align-items:center;justify-content:center}
.feature p{font-size:15px;margin-top:30px;line-height:1.5}
.feature .btn{margin-top:16px;width:82px;height:28px;line-height:28px;font-size:11px;border-radius:3px}

/* about */
.about-photo{left:0;top:1115px;width:1200px;height:476px;background:linear-gradient(90deg,#c8b3a6,#e2cfc4 45%,#e9d9d1 70%,#dfcdc4)}
.about-hands{left:80px;top:1160px;width:480px;height:380px;background:radial-gradient(ellipse,rgba(226,90,150,.55),rgba(226,90,150,0) 65%)}
.about-title{left:623px;top:1253px;font-family:"Raleway",sans-serif;font-weight:700;font-size:31px}
.about-rule{left:623px;top:1306px;width:70px;height:2px;background:var(--pink)}
.about-text{left:623px;top:1332px;width:440px;font-size:12.5px;line-height:1.75;color:#555}
.about-btns{left:623px;top:1474px;display:flex;gap:20px}
.about-btns .btn{width:115px;height:34px;line-height:34px;font-size:12px;border-radius:3px}

/* location form */
.loc-card{left:149px;top:1659px;width:902px;height:496px;background:#fff;box-shadow:0 3px 16px rgba(0,0,0,.15)}
.loc-head{height:129px;background:linear-gradient(var(--pink),#ee4a9b);color:#fff;text-align:center;padding-top:30px}
.loc-head h2{font-family:"Raleway",sans-serif;font-weight:800;font-size:27px}
.loc-head p{font-size:12.5px;margin-top:10px}
.loc-grid{display:grid;grid-template-columns:repeat(4,1fr);gap:14px 22px;padding:24px 32px 0}
.loc-grid .field{height:30px}
.mixed{display:flex;align-items:center;gap:8px;font-size:10px}
.mixed .field{flex:1}
.mini{width:52px;height:30px;background:var(--field);border-radius:3px;font-size:10px;color:#999;line-height:30px;padding-left:8px}
.message{margin:14px 32px 0;height:76px;background:var(--field);border-radius:3px;font-size:10px;color:#999;padding:10px 12px}
.loc-foot{position:absolute;left:32px;top:432px;width:838px;display:flex;align-items:center}
.check{width:14px;height:14px;border:1px solid #aaa;border-radius:2px;margin-right:14px;flex:none}
.loc-note{font-size:10.5px;line-height:1.7;width:460px;color:#555}
.loc-note span{color:var(--pink)}
.captcha{margin-left:auto;width:174px;height:46px;border:1px solid #d0d0d0;background:#f9f9f9;display:flex;align-items:center;padding-left:12px;font-size:10px;gap:10px}
.captcha i{width:18px;height:18px;border:2px solid #c1c1c1;background:#fff;display:block}
.loc-submit{margin-left:22px;width:96px;height:40px;line-height:40px;font-size:13px}

/* screening */
.screen-bg{left:0;top:2227px;width:1200px;height:329px;background:linear-gradient(90deg,#fdf1ef,#fbe6e6 50%,#f5c9d0)}
.screen-photo{left:640px;top:2227px;width:560px;height:329px;background:linear-gradient(90deg,rgba(248,214,220,0),#eaa3b4 45%,#e48aa2)}
.screen-title{left:149px;top:2321px;font-family:"Cinzel",serif;font-weight:600;font-size:26px;color:var(--pink)}
.screen-sub{left:149px;top:2372px;font-size:16px}
.screen-cta{left:149px;top:2427px;width:204px;height:36px;line-height:36px;font-size:13px}

/* faq */
.faq-rule{left:566px;top:2672px;width:68px;height:2px;background:var(--sky)}
.faq-col{width:430px;display:flex;flex-direction:column;gap:19px}
.faq-item{background:#ededed;border-radius:3px}
.faq-q{height:42px;display:flex;align-items:center;padding:0 14px;font-size:13px}
.faq-q .q{width:18px;height:18px;border-radius:50%;background:var(--pink);color:#fff;font-size:11px;font-weight:700;text-align:center;line-height:18px;margin-right:24px;flex:none}
.faq-q .pm{margin-left:auto;color:var(--pink);font-size:24px;font-weight:400;line-height:1}
.faq-a{padding:0 20px 14px 56px;font-size:11px;line-height:1.7;color:#555}

/* footer */
.footer{left:0;top:3006px;width:1200px;height:285px;background:var(--footer)}
.foot-col{top:3054px;color:#fff}
.foot-col h4{font-family:"Open Sans",sans-serif;font-weight:600;font-size:15px;margin-bottom:18px}
.foot-col p,.foot-col li{font-size:11px;color:#9a9a9a;line-height:1.9;list-style:none}
.socials{display:flex;gap:15px;margin-top:16px}
.socials span{width:32px;height:32px;border-radius:50%;background:var(--pink)}
.news{display:flex;margin-top:6px}
.news div{width:146px;height:40px;background:#fff;font-size:10px;color:#666;line-height:40px;padding-left:10px;border-radius:3px 0 0 3px}
.news b{width:56px;height:40px;background:var(--sky-dark);color:#fff;font-size:10.5px;line-height:40px;text-align:center;border-radius:0 3px 3px 0}
.foot-bottom{left:0;top:3225px;width:1200px;height:66px;border-top:1px solid #444;background:var(--footer-deep)}
.copy{left:149px;top:3248px;font-size:10.5px;color:#9a9a9a}
.legal{left:853px;top:3248px;font-size:10.5px;color:#9a9a9a}
</style>
</head>
<body>

<!-- header -->
<div class="abs topbar"></div>
<div class="abs navbar"></div>
<div class="abs brand">
  <span class="brand-dot"></span>
  <span class="brand-name">PINK ROAD<br>FOUNDATION</span>
</div>
<p class="abs tagline">Donate Your Car or Boat to Pink Road Foundation</p>
<p class="abs phone">Fast &amp; Free Pick Up<b>888-555-0142</b></p>
<span class="abs btn btn-pink top-cta">DONATE NOW!</span>
<ul class="abs menu">
  <li class="active">Home</li><li>How it works</li><li>Why donate your car</li><li>FAQ's</li><li>About us</li><li>Contact us</li>
</ul>

<!-- hero -->
<div class="abs hero-photo" role="img" aria-label="Black and white photo of a hand holding a pink awareness ribbon over weathered wood"></div>
<div class="abs hero-ribbon" aria-hidden="true"></div>
<form class="abs hero-form">
  <div class="hero-form-head">
    <h2>DONATE YOUR CAR TO PRF</h2>
    <p>Full Tax Deduction - Running or Not - No Paperwork Hassles - Help Fund Programs</p>
  </div>
  <div class="fields">
    <div class="field">Full Name</div><div class="field">Email Address</div>
    <div class="field">Phone Number</div><div class="field">Other Number</div>
    <div class="field">Address</div><div class="field">City</div>
    <div class="field">State</div><div class="field">Zip Code</div>
  </div>
  <span class="btn btn-pink hero-cta">DONATE NOW</span>
  <p class="hero-call">OR CALL TOLL-FREE: <span>888-555-0142</span></p>
</form>

<!-- donate -->
<h2 class="abs sec-title" style="top:692px">Donate Your Car</h2>
<p class="abs sec-sub" style="top:745px">Your car or boat donation helps support those stricken by breast cancer</p>
<div class="abs feature" style="left:179px;top:805px">
  <div class="feature-ring"><span><svg width="56" height="40" viewBox="0 0 56 40"><rect x="4" y="14" width="28" height="14" rx="2" fill="#fff"/><path d="M32 18h10l8 10H32z" fill="#fff"/><circle cx="14" cy="32" r="5" fill="#fff"/><circle cx="42" cy="32" r="5" fill="#fff"/><path d="M8 14L24 4" stroke="#fff" stroke-width="3"/></svg></span></div>
  <p>Fast Free Pickup -<br>24hr Response</p>
  <span class="btn btn-sky">More Info</span>
</div>
<div class="abs feature" style="left:467px;top:805px">
  <div class="feature-ring"><span><svg width="60" height="50" viewBox="0 0 60 50"><ellipse cx="30" cy="22" rx="24" ry="16" fill="none" stroke="#fff" stroke-width="3"/><text x="30" y="28" text-anchor="middle" fill="#fff" font-family="Raleway,sans-serif" font-weight="800" font-size="15">TAX</text><circle cx="20" cy="45" r="3" fill="#fff"/><circle cx="30" cy="45" r="3" fill="#fff"/><circle cx="40" cy="45" r="3" fill="#fff"/></svg></span></div>
  <p>Tax Deduction -<br>Easy To Do!</p>
  <span class="btn btn-sky">More Info</span>
</div>
<div class="abs feature" style="left:767px;top:805px">
  <div class="feature-ring"><span><svg width="52" height="52" viewBox="0 0 52 52"><path d="M10 30l5-12h22l5 12z" fill="#fff"/><rect x="6" y="30" width="40" height="10" rx="3" fill="#fff"/><circle cx="16" cy="44" r="4" fill="#fff"/><circle cx="36" cy="44" r="4" fill="#fff"/><path d="M26 4a6 6 0 0 1 6 6l-6 8-6-8a6 6 0 0 1 6-6z" fill="#fff"/></svg></span></div>
  <p>Running or not -<br>No Emission Test Required</p>
  <span class="btn btn-sky">More Info</span>
</div>

<!-- about -->
<div class="abs about-photo" role="img" aria-label="Soft photo of joined hands holding a pink ribbon"></div>
<div class="abs about-hands" aria-hidden="true"></div>
<h2 class="abs about-title">About Pink Road Foundation.</h2>
<div class="abs about-rule"></div>
<p class="abs about-text">Your car or boat donation helps support those stricken by breast cancer &amp; their families, and supports programs for screening, prevention, treatment and patient well being. Our operators are standing by 24 hours a day, 7 days a week to answer your questions and get your car or boat donation picked up quickly!</p>
<div class="abs about-btns"><span class="btn btn-pink">DONATE NOW</span><span class="btn btn-sky">LEARN MORE</span></div>

<!-- location form -->
<form class="abs loc-card">
  <div class="loc-head">
    <h2>YOUR CAR IS AT DIFFRENT LOCATION NO PROBLEM!</h2>
    <p>If your vehicle is at a different location, please provide detailed information:</p>
  </div>
  <div class="loc-grid">
    <div class="field">Pick-Up Street Address</div><div class="field">Pick-Up City</div><div class="field">Pick-Up State</div><div class="field">Pick-Up Zip Code</div>
    <div class="field">Email Address</div><div class="field">Day Phone</div><div class="field">Cell Phone</div><div class="field">Evening Phone</div>
    <div class="field">Vehicle Year</div><div class="field">Vehicle Make</div><div class="field">Vehicle Model</div><div class="field">Colour</div>
    <div class="field">Vin (If Available)</div><div class="field">Mileage</div>
    <div class="mixed"><div class="field">Running</div>Body Damage:<div class="mini">Yes</div></div>
    <div class="mixed">Do you have title?<div class="mini">Yes</div></div>
  </div>
  <div class="message">Message</div>
  <div class="loc-foot">
    <span class="check"></span>
    <p class="loc-note">We can accept cars with no title and/or in poor condition, but we may choose to send those to a different company for pickup... <span>Read More &gt;&gt;</span></p>
    <div class="captcha"><i></i>I'm not a robot</div>
    <span class="btn btn-sky loc-submit">SUBMIT</span>
  </div>
</form>

<!-- screening -->
<div class="abs screen-bg"></div>
<div class="abs screen-photo" role="img" aria-label="Photo of a woman in a pink shirt holding a pink ribbon to her chest"></div>
<h2 class="abs screen-title">Free Screening For Breast Cancer.</h2>
<p class="abs screen-sub">For You, For Friend &amp; For Someone In Your Family</p>
<span class="abs btn btn-pink screen-cta">Check Up Appointment Now!</span>

<!-- faq -->
<h2 class="abs sec-title" style="top:2614px">Frequently asked questions</h2>
<div class="abs faq-rule"></div>
<div class="abs faq-col" style="left:149px;top:2718px">
  <div class="faq-item"><div class="faq-q"><span class="q">?</span>Why donate a vehicle or vessel?<span class="pm">+</span></div></div>
  <div class="faq-item"><div class="faq-q"><span class="q">?</span>How does my vehicle or vessel donation...<span class="pm">+</span></div></div>
  <div class="faq-item"><div class="faq-q"><span class="q">?</span>How does donating a car or boat benefit my taxes?<span class="pm">+</span></div></div>
  <div class="faq-item"><div class="faq-q"><span class="q">?</span>How long does it take to pickup my donation?<span class="pm">+</span></div></div>
</div>
<div class="abs faq-col" style="left:621px;top:2718px">
  <div class="faq-item"><div class="faq-q"><span class="q">?</span>How do I donate a vehicle or vessel?<span class="pm">+</span></div></div>
  <div class="faq-item"><div class="faq-q"><span class="q">?</span>What happens to my car after it's picked up?<span class="pm">&minus;</span></div>
    <p class="faq-a">Most donated vehicles and vessels are towed. Pink Road Foundation works with over 100 auctions around the country to insure the highest sale price.</p></div>
  <div class="faq-item"><div class="faq-q"><span class="q">?</span>What kinds of donations can the charity accept?<span class="pm">+</span></div></div>
</div>

<!-- footer -->
<div class="abs footer"></div>
<div class="abs foot-col" style="left:149px;width:240px">
  <h4>About Pink Road Foundation</h4>
  <p>Your car or boat donation helps support those stricken by breast cancer &amp; their families, and supports programs for screening, prevention, treatment and patient well being.</p>
</div>
<div class="abs foot-col" style="left:447px">
  <h4>Quick Links</h4>
  <ul><li>Home</li><li>Donate Now</li><li>FAQs</li><li>Contact Us</li></ul>
</div>
<div class="abs foot-col" style="left:613px">
  <h4>Follow us</h4>
  <p>Please follow us on social media</p>
  <div class="socials"><span></span><span></span><span></span><span></span></div>
</div>
<div class="abs foot-col" style="left:844px">
  <h4>Subscribe Our Newsletter</h4>
  <div class="news"><div>Enter email</div><b>SUBMIT</b></div>
</div>
<div class="abs foot-bottom"></div>
<p class="abs copy">Copyright 2018 © giveautopinkribbon.org All Rights Reserved.</p>
<p class="abs legal">Terms &amp; Conditions &nbsp;|&nbsp; Privacy Policy</p>

</body>
</html>
```